London Based Property Finding Company - have logo already

We find property for private purchasers and investors in London, UK.  We work for the BUYER, whereas estate agencies/real estate companies work for the seller. We offer a much more personalised service to UK and overseas purchasers.

We would like the following:

*A double sided business card

*A letterhead

We have attached two versions of the logo. Each logo style is set on two different coloured backgrounds. Please choose one of the two designs, whichever you prefer or feel more comfortable with, and produce one in black and one in white background.

This applies to both pieces of stationery.

THE BUSINESS CARD:

We would like the company name placed on its own on one side of the card and the contact details and what we do on the other.

e.g.

SIDE 1:

BRAMWELL PROPERTY FINDERS

SIDE 2:

Owen Bramwell

t: 0208 394 2261

m: +44(0)7940 318 472

e: info@bramwellpropertyfinders.co.uk

w: bramwellpropertyfinders.co.uk

London Property Finders and Search Agents

I will leave the layout up to you, but a minimalist layout is preferred. If you would like to put additional detial or design on the card then that is up to, but not specified.

It is optional to have the company name on side 2, but if you do use it, please make it smaller. than on the 1st side.

The design needs to be simple, professional and not too in your face.

If you are using the black background design on side 1 for the logo, then maybe a white backgounnd can be used on side 2 with a black typeface.

The type face for the contacts details should be sans serif standard typeface. Please experiment with the desciprtion.

-

THE LETTERHEAD;

You can experiment with the layout for the letterhead. e.g logo centre aligned on the top of the page with the contact details and address at the bottom of the page OR the logo, description running along a bar on the top of the page with the contact details and website address at the bottom. Please try and experiment with this, but the less 'busy', the better.

Here is info that needs to be on the letterhead.

Bramwell Property Finders

t: 0208 394 2261

m: +44(0)7940 318 472

(PLEASE NOTE; the below company info must be placed at the bottom of the page as a footer, in small text.)

Pemberly Holdings Ltd Trading as Bramwell Property Finders, a company registered in England & Wales, No.5917302 , Registered office is 41 Kelmscott House, Ashdown Lane, London, SW9 7QJ, t: 0208 394 2261, m: +44(0)7940 318 472, e: info@bramwellpropertyfinders.co.uk

Best of luck!

Thank you

Dear Designer,

I have now attached the supporting files to this brief.

Thanks,

Owen Bramwell
Bramwell Property Finders

```html
<!DOCTYPE html>
<html lang="en">
<head>
<meta charset="utf-8">
<title>Bramwell Property Finders – Business Card Options</title>
<link href="https://fonts.googleapis.com/css2?family=Didact+Gothic&display=swap" rel="stylesheet">
<style>
  :root {
    --ink: #0b0b0b;
    --paper: #ffffff;
    --accent: #5bb8e8;
    --label: #111111;
    --shadow: rgba(0, 0, 0, 0.28);
  }
  * { margin: 0; padding: 0; box-sizing: border-box; }
  html, body {
    width: 1200px; height: 1004px; overflow: hidden;
    background: var(--paper);
  }
  .sheet { position: relative; width: 1200px; height: 1004px; }

  .option-number {
    position: absolute;
    font-family: "Didact Gothic", Arial, sans-serif;
    font-size: 52px; line-height: 1; color: var(--label);
  }

  .card {
    position: absolute; overflow: hidden;
    box-shadow: 1px 2px 5px var(--shadow);
  }
  .card--dark { background: var(--ink); }
  .card--light { background: var(--paper); }
  .card--landscape { width: 327px; height: 188px; }
  .card--portrait { width: 211px; height: 372px; }

  .band { position: absolute; left: 0; width: 100%; background: var(--ink); }

  .company-name {
    position: absolute;
    font-family: "Didact Gothic", Arial, sans-serif; font-weight: 400;
    color: var(--paper); line-height: 1; white-space: nowrap;
  }
  .company-name--large { font-size: 18px; }
  .company-name--medium { font-size: 13px; }
  .company-name--small { font-size: 11px; }

  .contact {
    position: absolute;
    font-family: "Didact Gothic", Arial, sans-serif;
    font-size: 9.5px; line-height: 1.38; color: var(--ink);
    white-space: nowrap;
  }
  .contact--reverse { color: var(--paper); }
  .contact__name { font-size: 12px; line-height: 1.3; }
  .contact__name--accent { color: var(--accent); font-size: 13px; }
  .contact__row { display: flex; }
  .contact__key { width: 16px; }
</style>
</head>
<body>
<main class="sheet">

  <!-- Option 1 -->
  <span class="option-number" style="left:98px; top:215px;">1</span>
  <section class="card card--dark card--landscape" style="left:167px; top:57px;">
    <div class="company-name company-name--large" style="right:30px; top:86px;">Bramwell Property Finders</div>
  </section>
  <section class="card card--light card--landscape" style="left:167px; top:253px;">
    <div class="band" style="top:30px; height:45px;">
      <div class="company-name company-name--small" style="right:22px; top:17px;">Bramwell Property Finders</div>
    </div>
    <div class="contact" style="left:16px; top:114px;">
      <div class="contact__name">owen bramwell</div>
      <div class="contact__row"><span class="contact__key">t:</span>0208 394 2261</div>
      <div class="contact__row"><span class="contact__key">m:</span>+44(0)7940 318 472</div>
      <div class="contact__row"><span class="contact__key">e:</span>info@bramwellpropertyfinders.co.uk</div>
      <div class="contact__row"><span class="contact__key">w:</span>bramwellpropertyfinders.co.uk</div>
    </div>
  </section>

  <!-- Option 2 -->
  <span class="option-number" style="left:685px; top:215px;">2</span>
  <section class="card card--dark card--landscape" style="left:743px; top:55px;">
    <div class="company-name company-name--large" style="right:30px; top:86px;">Bramwell Property Finders</div>
  </section>
  <section class="card card--light card--landscape" style="left:743px; top:250px;">
    <div class="band" style="top:33px; left:3px; width:160px; height:45px;">
      <div class="company-name company-name--small" style="right:10px; top:17px;">Bramwell Property Finders</div>
    </div>
    <div class="contact" style="left:17px; top:110px;">
      <div class="contact__name">owen bramwell</div>
      <div class="contact__row"><span class="contact__key">t:</span>0208 394 2261</div>
      <div class="contact__row"><span class="contact__key">m:</span>+44(0)7940 318 472</div>
      <div class="contact__row"><span class="contact__key">e:</span>info@bramwellpropertyfinders.co.uk</div>
      <div class="contact__row"><span class="contact__key">w:</span>bramwellpropertyfinders.co.uk</div>
    </div>
  </section>

  <!-- Option 3 -->
  <span class="option-number" style="left:72px; top:700px;">3</span>
  <section class="card card--light card--portrait" style="left:138px; top:522px;">
    <div class="band" style="top:162px; height:87px;">
      <div class="company-name company-name--medium" style="right:14px; top:37px;">Bramwell Property Finders</div>
    </div>
  </section>
  <section class="card card--dark card--portrait" style="left:358px; top:522px;">
    <div class="company-name company-name--small" style="right:12px; top:56px;">Bramwell Property Finders</div>
    <div class="contact contact--reverse" style="left:20px; top:290px;">
      <div class="contact__name contact__name--accent">owen bramwell</div>
      <div class="contact__row"><span class="contact__key">t:</span>0208 394 2261</div>
      <div class="contact__row"><span class="contact__key">m:</span>+44(0)7940 318 472</div>
      <div class="contact__row"><span class="contact__key">e:</span>info@bramwellpropertyfinders.co.uk</div>
      <div class="contact__row"><span class="contact__key">w:</span>bramwellpropertyfinders.co.uk</div>
    </div>
  </section>

  <!-- Option 4 -->
  <span class="option-number" style="left:645px; top:700px;">4</span>
  <section class="card card--light card--portrait" style="left:690px; top:523px;">
    <div class="band" style="top:163px; height:83px;">
      <div class="company-name company-name--medium" style="right:14px; top:35px;">Bramwell Property Finders</div>
    </div>
  </section>
  <section class="card card--light card--portrait" style="left:912px; top:523px;">
    <div class="band" style="top:163px; height:83px;">
      <div class="contact contact--reverse" style="left:12px; top:9px;">
        <div class="contact__name contact__name--accent">owen bramwell</div>
        <div class="contact__row"><span class="contact__key">t:</span>0208 394 2261</div>
        <div class="contact__row"><span class="contact__key">m:</span>+44(0)7940 318 472</div>
        <div class="contact__row"><span class="contact__key">e:</span>info@bramwellpropertyfinders.co.uk</div>
        <div class="contact__row"><span class="contact__key">w:</span>bramwellpropertyfinders.co.uk</div>
      </div>
    </div>
  </section>

</main>
</body>
</html>
```